Brisk Hollow Builders Needs A Flyer

We need a flyer for our newest product "The Cedarlane Garden Workroom"

Here is some copy for the flyer:

1. More and more people everyday are working from home and finding it difficult to disconnect from home activities in order to focus on their work. They are also finding it very expensive to add on to their existing house for a quiet place. Our archatectually stunning, Cedarlane Garden Workroom is the answer. The office studio measures 16' wide and 10' deep. 160 Square feet of space.

Perfect for dozens of purposes. Home office, design studio, artist studio, home school office, reading room, craft studio, drafting room.

Features include:

- Steel Framing. 40-60% lighter then wood, higher strength to weight ratio, resistant to mold and fire and steel is the most recycled material on earth!
- Spray foam insulation. Cool in the summer and warm in the winter.
- HVAC Mini Split with wireless remote control and thermostat.
- 100% Off grid with enough solar and battery storage to run your entire office. No need to pay for an expensive electric installation.
- Flush fitting floor outlets to reduce wires.
- TV mount (Optional with pre-wired electric, HDMI, digital audio & Cat 6)
- Windows are tempered glass custom made by Morvik Glazing.
- Solar qualifies for a 26% tax credit. This is not a write-off rather it is a direct reduction on your tax obligation.
- Thousands of dollars less than adding onto your home.
- Custom color, siding, features available.

This beautiful back yard office is delivered 100% assembled and ready to enjoy on the day of delivery.

We ship nationwide from our factory in South Carolina. Give us a call anytime to speak to a designer and start your dream office today!

555-318-4027
info@BriskHollowBuilders.example

```html
<!DOCTYPE html>
<html lang="en">
<head>
<meta charset="utf-8">
<title>Brisk Hollow Builders – Cedarlane Garden Workroom Flyer</title>
<link rel="stylesheet" href="https://fonts.googleapis.com/css2?family=Rubik:wght@400;500;600;700&family=Roboto:wght@400;500;700&display=swap">
<style>
:root{
  --green:#5c9e3b;
  --green-dark:#3f7f2a;
  --green-light:#7cb850;
  --gold:#f5b324;
  --gold-dark:#e89a12;
  --ink:#2e2e2e;
  --muted:#444;
  --paper:#ffffff;
  --backdrop:#c9c9c9;
  --photo-a:#9fb7c9;
  --photo-b:#5b5f5e;
  --thumb-a:#e9e9e9;
  --thumb-b:#3b3b3b;
}
*{box-sizing:border-box;margin:0;padding:0}
html,body{width:1200px;height:1200px;overflow:hidden}
body{background:var(--backdrop);position:relative;font-family:"Roboto",sans-serif;color:var(--ink)}
.page{position:absolute;top:228px;width:527px;height:745px;background:var(--paper);overflow:hidden;box-shadow:0 4px 10px rgba(0,0,0,.25)}
.page-front{left:65px}
.page-back{left:610px}
.abs{position:absolute}
.swoosh{position:absolute;left:0;width:100%}

/* front */
.brand{left:30px;top:48px;display:flex;align-items:center;gap:8px}
.brand-dot{width:20px;height:20px;border-radius:50%;background:var(--green)}
.brand-name{font-family:"Rubik",sans-serif;font-weight:700;font-size:14px;color:var(--green);letter-spacing:.2px;text-transform:uppercase;line-height:1}
.title-band{left:0;top:115px;width:330px;height:121px;background:var(--green);padding:18px 0 0 42px}
.title-band h1{font-family:"Rubik",sans-serif;color:#fff;text-transform:uppercase;line-height:1}
.title-band .t1{display:block;font-size:24px;font-weight:600}
.title-band .t2{display:block;font-size:36px;font-weight:700;margin-top:2px}
.title-band .t3{display:block;font-size:20px;font-weight:600;color:var(--gold);margin-top:3px}
.hero{top:0;left:0;width:527px;height:262px}
.intro{left:38px;top:257px;width:462px;font-size:11.3px;line-height:1.32;color:var(--muted)}
.thumbs{left:25px;top:338px;display:flex;gap:17px}
.thumb{width:148px;height:125px;border:3px solid var(--gold);border-radius:10px;padding:18px 14px;background:#fff}
.thumb-art{width:100%;height:100%;background:linear-gradient(180deg,var(--thumb-a) 0%,#cfcfcf 40%,var(--thumb-b) 100%);border-radius:2px}
.pill{height:29px;border-radius:15px;background:linear-gradient(180deg,var(--green-light),var(--green-dark));color:#fff;font-family:"Rubik",sans-serif;display:flex;align-items:center;justify-content:center;box-shadow:0 0 0 2px #e3efd9}
.purposes-pill{left:21px;top:485px;width:484px;font-size:12px;font-weight:600;text-transform:uppercase}
.uses{display:flex}
.use{display:flex;flex-direction:column;align-items:center;width:82px}
.use-label{font-size:12px;font-weight:500;margin-top:5px;white-space:nowrap}
.tick{width:38px;height:38px}
.connector{width:20px;display:flex;align-items:center;justify-content:center;height:38px}
.connector span{width:8px;height:8px;border-radius:50%;border:2px solid var(--gold);background:#fff}
.uses-row1{left:51px;top:540px}
.uses-row2{left:120px;top:622px}

/* back */
.inset{left:321px;top:8px;width:150px;height:150px;border-radius:50%;border:6px solid var(--gold);background:linear-gradient(160deg,#f4f4f4,#dcdcdc)}
.features-pill{left:41px;top:188px;width:447px;height:29px;font-size:18px;font-weight:600}
.features{top:231px;display:flex;flex-direction:column;gap:13px;list-style:none}
.features-left{left:37px;width:222px}
.features-right{left:281px;width:212px}
.features li{position:relative;padding-left:15px;font-size:10.4px;line-height:14.4px;color:var(--muted)}
.features li::before{content:"";position:absolute;left:0;top:3px;width:8px;height:8px;border:1.5px solid var(--green);border-radius:50%}
.features li::after{content:"";position:absolute;left:3.5px;top:5px;width:2px;height:4px;border:solid var(--green);border-width:0 1.3px 1.3px 0;transform:rotate(45deg)}
.delivery{left:0;top:466px;width:527px;height:130px;background:linear-gradient(180deg,var(--green-light),var(--green) 60%,var(--green-dark));text-align:center;color:#fff}
.delivery h2{font-family:"Rubik",sans-serif;font-size:15px;font-weight:600;line-height:17px;text-transform:uppercase;margin-top:14px}
.delivery hr{border:0;border-top:1px solid rgba(255,255,255,.55);width:440px;margin:14px auto 0}
.ship{margin-top:11px;font-family:"Rubik",sans-serif;font-size:12px;font-weight:500;display:flex;justify-content:center;align-items:center;gap:8px}
.ship i{width:5px;height:5px;border-radius:50%;background:var(--gold)}
.cta{left:0;width:527px;top:613px;text-align:center;font-family:"Rubik",sans-serif;font-size:11.5px;font-weight:500;color:var(--green)}
.phone{left:0;width:527px;top:632px;display:flex;justify-content:center;align-items:center;gap:14px}
.phone-icon{width:32px;height:32px}
.phone-number{font-family:"Rubik",sans-serif;font-size:42px;font-weight:600;color:var(--ink);letter-spacing:.5px;line-height:48px}
.email{left:0;width:527px;top:682px;text-align:center;font-family:"Rubik",sans-serif;font-size:16px;font-weight:500;color:var(--ink)}
</style>
</head>
<body>

<section class="page page-front">
  <div class="abs title-band">
    <h1><span class="t1">The Cedarlane</span><span class="t2">Garden</span><span class="t3">Workroom</span></h1>
  </div>

  <svg class="abs hero" viewBox="0 0 527 262">
    <defs>
      <linearGradient id="heroPhoto" x1="0" y1="0" x2="0" y2="1">
        <stop offset="0" stop-color="var(--photo-a)"/>
        <stop offset=".45" stop-color="#8a8f8c"/>
        <stop offset="1" stop-color="var(--photo-b)"/>
      </linearGradient>
    </defs>
    <path d="M300,115 C340,200 430,240 527,250 V262 H527 C420,258 320,215 280,140 Z" fill="var(--gold)"/>
    <path d="M268,120 C320,210 430,244 527,246 V238 C440,230 340,190 300,115 Z" fill="var(--green)"/>
    <path d="M262,0 H527 V236 C440,228 345,190 300,110 C285,80 268,40 262,0 Z" fill="url(#heroPhoto)" role="img" aria-label="Photo of the garden workroom studio with glass doors on a patio"/>
  </svg>

  <div class="abs brand"><span class="brand-dot"></span><span class="brand-name">Brisk Hollow Builders</span></div>

  <p class="abs intro">More and more people everyday are working from home and finding it difficult to disconnect from home activities in order to focus on their work. They are also finding it very expensive to add on to their existing house for a quiet place. Our archatectually stunning, Cedarlane Garden Workroom is the answer. The office studio measures 16' wide and 10' deep. 160 Square feet of space.</p>

  <div class="abs thumbs">
    <div class="thumb"><div class="thumb-art" role="img" aria-label="Render of the workroom, front three-quarter view"></div></div>
    <div class="thumb"><div class="thumb-art" role="img" aria-label="Render of the workroom, front view"></div></div>
    <div class="thumb"><div class="thumb-art" role="img" aria-label="Render of the workroom, side three-quarter view"></div></div>
  </div>

  <div class="abs pill purposes-pill">Perfect for dozens of purposes.</div>

  <div class="abs uses uses-row1">
    <div class="use"><svg class="tick" viewBox="0 0 40 40"><circle cx="20" cy="20" r="17" fill="var(--green)" stroke="#dfeed3" stroke-width="4"/><path d="M12 20.5l6 6 11-13" fill="none" stroke="#fff" stroke-width="4" stroke-linecap="round" stroke-linejoin="round"/></svg><span class="use-label">Home office,</span></div>
    <div class="connector"><span></span></div>
    <div class="use"><svg class="tick" viewBox="0 0 40 40"><circle cx="20" cy="20" r="17" fill="var(--green)" stroke="#dfeed3" stroke-width="4"/><path d="M12 20.5l6 6 11-13" fill="none" stroke="#fff" stroke-width="4" stroke-linecap="round" stroke-linejoin="round"/></svg><span class="use-label">design studio,</span></div>
    <div class="connector"><span></span></div>
    <div class="use"><svg class="tick" viewBox="0 0 40 40"><circle cx="20" cy="20" r="17" fill="var(--green)" stroke="#dfeed3" stroke-width="4"/><path d="M12 20.5l6 6 11-13" fill="none" stroke="#fff" stroke-width="4" stroke-linecap="round" stroke-linejoin="round"/></svg><span class="use-label">artist studio,</span></div>
    <div class="connector"><span></span></div>
    <div class="use"><svg class="tick" viewBox="0 0 40 40"><circle cx="20" cy="20" r="17" fill="var(--green)" stroke="#dfeed3" stroke-width="4"/><path d="M12 20.5l6 6 11-13" fill="none" stroke="#fff" stroke-width="4" stroke-linecap="round" stroke-linejoin="round"/></svg><span class="use-label">home school office,</span></div>
  </div>

  <div class="abs uses uses-row2">
    <div class="use"><svg class="tick" viewBox="0 0 40 40"><circle cx="20" cy="20" r="17" fill="var(--green)" stroke="#dfeed3" stroke-width="4"/><path d="M12 20.5l6 6 11-13" fill="none" stroke="#fff" stroke-width="4" stroke-linecap="round" stroke-linejoin="round"/></svg><span class="use-label">reading room,</span></div>
    <div class="connector"><span></span></div>
    <div class="use"><svg class="tick" viewBox="0 0 40 40"><circle cx="20" cy="20" r="17" fill="var(--green)" stroke="#dfeed3" stroke-width="4"/><path d="M12 20.5l6 6 11-13" fill="none" stroke="#fff" stroke-width="4" stroke-linecap="round" stroke-linejoin="round"/></svg><span class="use-label">craft studio,</span></div>
    <div class="connector"><span></span></div>
    <div class="use"><svg class="tick" viewBox="0 0 40 40"><circle cx="20" cy="20" r="17" fill="var(--green)" stroke="#dfeed3" stroke-width="4"/><path d="M12 20.5l6 6 11-13" fill="none" stroke="#fff" stroke-width="4" stroke-linecap="round" stroke-linejoin="round"/></svg><span class="use-label">drafting room.</span></div>
  </div>

  <svg class="swoosh" style="top:672px;height:73px" viewBox="0 0 527 73" preserveAspectRatio="none" aria-hidden="true">
    <path d="M0,0 C160,44 360,44 527,22 V73 H0 Z" fill="var(--green)"/>
    <path d="M0,18 C160,58 360,56 527,38 V73 H0 Z" fill="var(--gold)"/>
    <path d="M0,40 C170,73 360,70 527,56 V73 H0 Z" fill="var(--gold-dark)"/>
  </svg>
</section>

<section class="page page-back">
  <svg class="abs" style="left:0;top:0;width:527px;height:175px" viewBox="0 0 527 175">
    <defs>
      <linearGradient id="backPhoto" x1="0" y1="0" x2="0" y2="1">
        <stop offset="0" stop-color="var(--photo-a)"/>
        <stop offset=".5" stop-color="#6d6b66"/>
        <stop offset="1" stop-color="#7f8a6a"/>
      </linearGradient>
    </defs>
    <path d="M0,112 C160,160 360,135 527,52 V90 C360,165 150,175 0,140 Z" fill="var(--gold)"/>
    <path d="M0,104 C160,148 360,125 527,42 V62 C360,145 160,162 0,124 Z" fill="var(--green)"/>
    <path d="M0,0 H527 V42 C360,125 160,148 0,104 Z" fill="url(#backPhoto)" role="img" aria-label="Photo of the workroom exterior with solar panels on the roof in a planted garden"/>
  </svg>
  <div class="abs inset" role="img" aria-label="Drawing of the steel frame structure"></div>

  <div class="abs pill features-pill">Features Include</div>

  <ul class="abs features features-left">
    <li>Steel Framing. 40-60% lighter then wood, higher strength to weight ratio, resistant to mold and fire and steel is the most recycled material on earth!</li>
    <li>Spray foam insulation. Cool in the summer and warm in the winter.</li>
    <li>HVAC Mini Split with wireless remote control and thermostat.</li>
    <li>100% Off grid with enough solar and battery storage to run your entire office. No need to pay for an expensive electric installation.</li>
  </ul>
  <ul class="abs features features-right">
    <li>Flush fitting floor outlets to reduce wires.</li>
    <li>TV mount (Optional with pre-wired electric, HDMI, digital audio &amp; Cat 6)</li>
    <li>Windows are tempered glass custom made by Morvik Glazing.</li>
    <li>Solar qualifies for a 26% tax credit. This is not a write-off rather it is a direct reduction on your tax obligation.</li>
    <li>Thousands of dollars less than adding onto your home.</li>
    <li>Custom color, siding, features available.</li>
  </ul>

  <div class="abs delivery">
    <h2>This beautiful back yard office is delivered<br>100% assembled and ready to enjoy on<br>the day of delivery.</h2>
    <hr>
    <p class="ship"><i></i>We ship nationwide from our factory in South Carolina.<i></i></p>
  </div>

  <p class="abs cta">Give us a call anytime to speak to a designer and start your dream office today!</p>

  <div class="abs phone">
    <svg class="phone-icon" viewBox="0 0 34 34" aria-hidden="true"><circle cx="17" cy="17" r="17" fill="var(--gold)"/><path d="M12.5 9.5c.8-.4 1.6-.2 2 .6l1.4 2.8c.3.7.2 1.4-.4 1.9l-1 .9c.8 1.8 2.1 3.1 3.9 3.9l.9-1c.5-.6 1.2-.7 1.9-.4l2.8 1.4c.8.4 1 1.2.6 2l-.8 1.5c-.5.9-1.5 1.4-2.5 1.2-5-1.1-8.6-4.7-9.7-9.7-.2-1 .3-2 1.2-2.5z" fill="#fff"/></svg>
    <span class="phone-number">555-318-4027</span>
  </div>
  <p class="abs email">info@BriskHollowBuilders.example</p>

  <svg class="swoosh" style="top:708px;height:37px" viewBox="0 0 527 37" preserveAspectRatio="none" aria-hidden="true">
    <path d="M0,8 C170,26 360,24 527,2 V37 H0 Z" fill="var(--green)"/>
    <path d="M0,17 C170,33 360,30 527,11 V37 H0 Z" fill="var(--gold)"/>
  </svg>
</section>

</body>
</html>
```